Business Card for Restaurant Vendal

This project consist of creating 2 design for business card of restaurant named Vendal.

The attached specs below are 'ONLY SUGGESTION' if you have others ideas. You are welcome to post it.

1) Restaurant Card

Adresse:
2784 Côte du Pinard Vert
Montréal (Qc) H4K 3T8

Website:
www.ven-dal.ca

Phone:
438-719-2046

2) Employee Card

Name: Lorna Pik
Title: Owner

Address:
2784 Côte du Pinard Vert
Montréal (Qc) H4K 3T8

Email:lorna@ven-dal.ca
Phone Number:438-719-2046
Cellphone Number:514-830-4162

 The attached specs are 'ONLY SUGGESTION' if you have others ideas.  You are welcome to post it.

Industry/Entity Type

Restaurant

Requirements
Must have
• UV Card Spot

To print Spot UV business cards you would have to submit 2 files for each side. The first file "base" would be your regular design file as it would have been in any other case. The 2nd file "UV mask" is a black/white file. The BLACK color will indicate the areas that will be covered with the UV high gloss finish. To upload the files, please combine front design and front mask file in one P
Nice to have
• 1) The font of the logo should be ink effect
2) black background with wallpaper effect
3) The specs below are 'ONLY SUGGESTION' if you have others ideas. You are welcome to post it.

```html
<!DOCTYPE html>
<html lang="fr">
<head>
<meta charset="utf-8">
<title>Restaurant Vendal – Business Cards</title>
<link rel="stylesheet" href="https://fonts.googleapis.com/css2?family=Open+Sans:wght@400;600;700&family=PT+Sans:wght@400&display=swap">
<style>
  :root {
    --page: #ececec;
    --ink: #111111;
    --card-dark: #050505;
    --card-light: #ffffff;
    --red: #e5332a;
    --red-deep: #b8211a;
    --white: #ffffff;
    --text-dark: #1a1a1a;
  }
  * { box-sizing: border-box; margin: 0; padding: 0; }
  html, body {
    width: 1200px; height: 1000px; overflow: hidden;
    background: var(--page);
  }
  .canvas {
    position: relative; width: 1200px; height: 1000px;
  }
  .card {
    position: absolute; left: 230px; width: 740px; height: 420px;
    box-shadow: 0 6px 18px rgba(0,0,0,.18);
  }

  /* Front card */
  .card--front { top: 60px; background: var(--card-dark); }
  .lantern {
    position: absolute; border-radius: 50%;
  }
  .card--front .lantern {
    left: 40px; top: 105px; width: 250px; height: 250px;
    background: radial-gradient(circle at 45% 35%, var(--red) 0%, var(--red-deep) 55%, #2a2a2a 100%);
    box-shadow: 0 0 24px rgba(255,255,255,.35);
  }
  .brand {
    position: absolute; left: 330px; top: 140px;
    display: flex; align-items: center; gap: 14px;
  }
  .brand__name {
    font-family: "Open Sans", sans-serif; font-weight: 700;
    font-size: 96px; line-height: 1; color: var(--white);
    letter-spacing: 1px;
  }
  .brand__dot {
    width: 22px; height: 22px; border-radius: 50%; background: var(--red);
  }
  .tagline {
    position: absolute; left: 334px; top: 270px;
    font-family: "PT Sans", sans-serif; font-size: 19px; color: var(--white);
  }
  .tagline .sep { color: var(--red); margin: 0 6px; }

  /* Back card */
  .card--back { top: 520px; background: var(--card-light); }
  .holder {
    position: absolute; left: 60px; top: 60px;
    display: flex; align-items: flex-start; gap: 30px;
  }
  .holder__icon { width: 60px; height: 66px; }
  .holder__name {
    font-family: "Open Sans", sans-serif; font-weight: 700;
    font-size: 30px; color: var(--text-dark); line-height: 1.1;
  }
  .holder__title {
    font-family: "Open Sans", sans-serif; font-weight: 400;
    font-size: 26px; letter-spacing: 6px; color: var(--text-dark);
  }
  .contacts {
    position: absolute; left: 80px; top: 190px; list-style: none;
    font-family: "Open Sans", sans-serif; font-size: 17px; color: var(--text-dark);
  }
  .contacts li {
    display: flex; align-items: center; gap: 40px; margin-bottom: 18px;
    line-height: 1.3;
  }
  .contacts svg { width: 26px; height: 26px; flex: none; fill: var(--red); }
  .card--back .lantern {
    right: 70px; top: 80px; width: 250px; height: 250px;
    background: linear-gradient(180deg, var(--red) 0%, var(--red-deep) 65%, #f4e6e4 100%);
  }
</style>
</head>
<body>
<main class="canvas">

  <section class="card card--front" aria-label="Restaurant card, front">
    <div class="lantern" role="img" aria-label="Illustration of a red paper lantern glowing on black"></div>
    <div class="brand">
      <span class="brand__name">Vendal</span>
      <span class="brand__dot"></span>
    </div>
    <p class="tagline">Resto-Bar Japonais<span class="sep">•</span>Izakaya<span class="sep">•</span>居酒屋</p>
  </section>

  <section class="card card--back" aria-label="Employee card, back">
    <div class="holder">
      <svg class="holder__icon" viewBox="0 0 60 66" aria-hidden="true">
        <circle cx="30" cy="18" r="16" fill="var(--red)"/>
        <path d="M0 66 C0 44 12 36 30 36 C48 36 60 44 60 66 Z" fill="var(--red)"/>
      </svg>
      <div>
        <p class="holder__name">Lorna Pik</p>
        <p class="holder__title">Owner</p>
      </div>
    </div>

    <ul class="contacts">
      <li>
        <svg viewBox="0 0 24 24" aria-hidden="true"><path d="M12 1a8 8 0 0 0-8 8c0 6 8 14 8 14s8-8 8-14a8 8 0 0 0-8-8zm0 11a3 3 0 1 1 0-6 3 3 0 0 1 0 6z"/></svg>
        <span>2784 Côte du Pinard Vert<br>Montréal (Qc) H4K 3T8</span>
      </li>
      <li>
        <svg viewBox="0 0 24 24" aria-hidden="true"><path d="M6.6 10.8a15 15 0 0 0 6.6 6.6l2.2-2.2c.3-.3.7-.4 1-.2 1.1.4 2.3.6 3.6.6.6 0 1 .4 1 1V20c0 .6-.4 1-1 1A17 17 0 0 1 3 4c0-.6.4-1 1-1h3.5c.6 0 1 .4 1 1 0 1.3.2 2.5.6 3.6.1.3 0 .7-.2 1z"/></svg>
        <span>438-719-2046</span>
      </li>
      <li>
        <svg viewBox="0 0 24 24" aria-hidden="true"><path d="M4 3h16a2 2 0 0 1 2 2v14a2 2 0 0 1-2 2H4a2 2 0 0 1-2-2V5a2 2 0 0 1 2-2zm1 3v10h14V6zm7 11.5a1.2 1.2 0 1 0 0 2.4 1.2 1.2 0 0 0 0-2.4z"/></svg>
        <span>514-830-4162</span>
      </li>
      <li>
        <svg viewBox="0 0 24 24" aria-hidden="true"><path d="M2 5h20v3l-10 6L2 8zm0 5 10 6 10-6v9H2z"/></svg>
        <span>lorna@ven-dal.ca</span>
      </li>
    </ul>

    <div class="lantern" role="img" aria-label="Illustration of a red paper lantern with brushed izakaya characters"></div>
  </section>

</main>
</body>
</html>
```